Geschäftspapiere für Beratungsleistung
Zielgruppe
DieKlarwerkstatt.com ist eine Beratungsleistung der Voltrin Consulting GmbH.
Wir beraten kleine und mittlere Unternehmen (B2B) in Fragen des Datenschutz. Wir unterstützen unsere Kunden dabei, die notwendigen Richtlinien, Dokumentationen und Prozesse einzuführen, die sicherstellen, dass unsere Kunden die gesetzlichen Vorgaben zum Schutz personenbezogener Daten einhalten.
Aufgabenstellung
Wichtiger Hinweis: Wir möchten die Gestaltung von Briefpapier und Visitenkarten beauftragen. Da grafikfinder.de das nicht als Standardprojekt mit entsprechender Preisskala vorsieht, haben wir einen individuellen Preis festgelegt (160 Euro Briefbogen + 120 Euro Visitenkarten).
'Die Klarwerkstatt' ist eine Marke der Voltrin Consulting GmbH. Das Markenlogo ist bereits vorhanden.
Die Aufgabenstellung ist es, einen Briefbogen mit den Geschäftsangaben, sowie einen Folgebogen ohne Geschäftsangaben zu entwickeln. Außerdem sollen Visitenkarten entworfen werden.
Die Geschäftspapiere sollen sich in der Gestaltung an die Website von 'Die Klarwerkstatt' anlehnen. Da die Website noch nicht live sind, ist der Entwurf der Homepage angehängt. Wichtig: die im Banner verwendete Teaser-Grafik soll nicht als Hintergrund für die Geschäftspapiere verwendet werden.
Bitte beachten Sie, dass 'Die Klarwerkstatt' kein Unternehmen ist, sondern eine Marke der Voltrin Consulting ist. Die Angaben auf den Geschäftspapieren beziehen sich daher auf die Voltrin Consulting GmbH. Der Briefbogen der Voltrin Consulting ist angehängt. Dort können die Geschäftsangaben entnommen werden. Das Voltrin Logo soll auf den Geschäftspapieren für 'Die Klarwerkstatt' nicht verwendet werden. Der Entwurf soll auf das Logo und Erscheinungsbild von 'Die Klarwerkstatt' abgestellt werden.
Die Entwürfe möchten wir zum einen im Indesign-Format haben, um diese an einen Druckdienstleister weiterzugeben bzw. die entsprechenden pdfs nach Vorgaben der Druckerei erzeugen zu können. Den Briefbogen und den Folgebogen möchten wir außerdem im Microsoft Word-Format haben, um Geschäftsbriefe direkt aus Word heraus zu erzeugen zu können. Die Dokumente sollen dann entweder als pdf per E-Mail versendet oder auf einem Tintenstrahldrucker gedruckt werden. Das Design sollte also auch auf einem Büro-Farbtintenstrahldrucker in guter Darstellung gedruc..

```html
<!DOCTYPE html>
<html lang="de">
<head>
<meta charset="utf-8">
<title>Die Klarwerkstatt – Briefbogen</title>
<link rel="stylesheet" href="https://fonts.googleapis.com/css2?family=Open+Sans:wght@400;600;700&family=Arimo:wght@400&display=swap">
<style>
  :root {
    --brand-blue: #0a4ea2;
    --ink: #1e1e1e;
    --body-ink: #3a3a3a;
    --muted: #6a6a6a;
    --backdrop: #d9d9d9;
    --paper: #ffffff;
    --fold-mark: #c8c8c8;
    --sig-tone: #ececec;
  }
  * { margin: 0; padding: 0; box-sizing: border-box; }
  html, body { width: 1200px; height: 968px; overflow: hidden; }
  body {
    background: var(--backdrop);
    font-family: "Open Sans", sans-serif;
    color: var(--ink);
    position: relative;
  }
  .letterhead {
    position: absolute;
    left: 275px; top: 24px;
    width: 650px; height: 920px;
    background: var(--paper);
    border-top: 5px solid var(--brand-blue);
    box-shadow: 0 4px 18px rgba(0,0,0,0.18);
  }
  .fold-mark {
    position: absolute; left: 0; width: 16px; height: 1px;
    background: var(--fold-mark);
  }
  .fold-mark.upper { top: 270px; }
  .fold-mark.punch { top: 450px; }
  .fold-mark.lower { top: 618px; }

  .brand {
    position: absolute; right: 46px; top: 62px;
    display: flex; align-items: center; gap: 10px;
  }
  .brand-square { width: 18px; height: 18px; background: var(--brand-blue); }
  .brand-name {
    font-weight: 700; font-size: 24px; letter-spacing: 0.5px;
    color: var(--brand-blue); text-transform: uppercase; line-height: 1;
  }

  .contact {
    position: absolute; left: 432px; top: 132px;
    border-left: 1px solid var(--brand-blue);
    padding-left: 16px;
    font-style: normal;
    font-size: 10.5px; line-height: 15px; color: var(--ink);
    white-space: nowrap;
  }
  .contact-row { display: flex; align-items: center; gap: 6px; }
  .contact-row svg { width: 10px; height: 10px; fill: var(--brand-blue); flex: none; }

  .sender-line {
    position: absolute; left: 70px; top: 118px; width: 255px;
    font-size: 6.5px; color: var(--ink); white-space: nowrap;
    border-bottom: 1px solid var(--muted); padding-bottom: 2px;
  }
  .recipient {
    position: absolute; left: 70px; top: 238px;
    font-family: "Arimo", sans-serif; font-size: 11px; color: var(--body-ink);
  }
  .letter-body {
    position: absolute; left: 70px; top: 262px; width: 480px;
    font-family: "Arimo", sans-serif; font-size: 11px; line-height: 14.5px;
    color: var(--body-ink);
  }
  .letter-body p { margin-bottom: 8px; }
  .signature {
    position: absolute; left: 70px; top: 590px;
    width: 180px; height: 46px; background: var(--sig-tone);
  }

  .footer {
    position: absolute; left: 0; right: 0; bottom: 0;
    border-bottom: 14px solid var(--brand-blue);
    height: 118px;
    display: grid; grid-template-columns: 190px 150px 170px;
    padding: 20px 70px 0;
    font-size: 10.5px; line-height: 15px; color: var(--ink);
    white-space: nowrap;
  }
  .footer-col { padding-left: 14px; }
  .footer-col + .footer-col { border-left: 1px solid var(--brand-blue); }
  .footer-col:first-child { padding-left: 0; }
</style>
</head>
<body>
  <main class="letterhead">
    <span class="fold-mark upper"></span>
    <span class="fold-mark punch"></span>
    <span class="fold-mark lower"></span>

    <div class="brand">
      <span class="brand-square"></span>
      <span class="brand-name">Die Klarwerkstatt</span>
    </div>

    <div class="sender-line">Voltrin Consulting GmbH | Lindenhofweg 7 B | 82041 Eichental</div>

    <address class="contact">
      <div>Voltrin Consulting GmbH</div>
      <div>Lindenhofweg 7 B</div>
      <div>D-82041 Eichental</div>
      <div class="contact-row">
        <svg viewBox="0 0 10 10"><path d="M2 0.5l2 2-1 1.2c.6 1.3 1.6 2.3 2.9 2.9l1.2-1 2 2-1.2 1.6C4.6 8.9 1.1 5.4.4 1.7z"/></svg>
        +49 89 550372-00</div>
      <div class="contact-row">
        <svg viewBox="0 0 10 10"><rect x="1" y="3" width="8" height="6"/><rect x="2.5" y="0.5" width="5" height="2"/></svg>
        +49 89 550372-09</div>
      <div class="contact-row">
        <svg viewBox="0 0 10 10"><rect x="0.5" y="2" width="9" height="6"/></svg>
        info@die-klarwerkstatt.com</div>
      <div class="contact-row">
        <svg viewBox="0 0 10 10"><circle cx="5" cy="5" r="4.5"/></svg>
        www.die-klarwerkstatt.com</div>
    </address>

    <div class="recipient">Herr Albrecht</div>

    <section class="letter-body">
      <p>Lorem ipsum dolor sit amet, consectetur adipiscing elit. Proin tincidunt, lectus id malesuada cursus, lorem augue egestas magna, ut mattis orci ante ut arcu. Sed mauris tellus, fermentum quis ligula nec, posuere pulvinar eros. Nam at mi quis velit pellentesque finibus. Donec lacus velit, faucibus mollis dolor nec, finibus pellentesque orci. Duis sed dictum elit, ut posuere arcu. Phasellus ac dolor et ante consequat rutrum nec nec tortor. Donec consequat, nibh sit amet pulvinar faucibus, turpis magna venenatis diam, vel pretium eros erat vestibulum nulla.</p>
      <p>Sed pretium ac enim eu viverra. Aliquam ac est eget magna convallis convallis. Aenean augue purus, finibus eget turpis quis, finibus dignissim nibh. Phasellus viverra lobortis dignissim. Duis varius turpis in sapien accumsan facilisis. Sed vehicula gravida diam a interdum. Nullam convallis ligula id erat egestas consequat. Integer consectetur ex vel aliquet iaculis. Vestibulum molestie sodales mauris, at tincidunt risus pellentesqu.</p>
      <p>Mauris facilisis, lectus at accumsan tincidunt, dui magna imperdiet sem, quis tempor est lectus eu ipsum. Praesent in fermentum nisl. Maecenas at lorem at odio interdum iaculis. Pellentesque cursus nulla nunc, ut suscipit nulla maximus et. Donec maximus rhoncus metus, vel laoreet nisi pretium sit amet. Donec posuere enim lectus, vitae aliquam augue tincidunt dignissim. Morbi vitae congue velit, quis elementum.</p>
    </section>

    <div class="signature" role="img" aria-label="Handschriftliche Unterschrift von Marlene Okafor"></div>

    <footer class="footer">
      <div class="footer-col">
        <div>Geschäftsführerin: Marlene Okafor</div>
        <div>Geschäftsführer: Jonas Velten</div>
      </div>
      <div class="footer-col">
        <div>Amtsgericht Eichental</div>
        <div>HRB 318572</div>
        <div>USt-ID: DE301475826</div>
      </div>
      <div class="footer-col">
        <div>Die Klarwerkstatt</div>
        <div>ist ein Beratungsangebot</div>
        <div>der Voltrin Consulting GmbH</div>
      </div>
    </footer>
  </main>
</body>
</html>
```